retro/vintage voucher design project

We are a concept bar in St Kilda (Australia). The bar is themed as a New York style loft apartment and has a retro/60's theme to it- we also use Rex Fennimore style pop art in a lot of our design elements. Please check out our website for direction (www.17thparlour.com.au)

We need a flyer/voucher designed as a promotional give out to potential customers looking to hold an event at our venue (such as a birthday party, xmas party etc...)

We need the flyer to be A6 size or DL size of any orientation and needs to be double sided.

We need the style of the flyer to reflect the style of our venue...I would also like to have an image of a person/persons having fun somewhere on the voucher

I have attached the flyer we have used up until now- but I want to update this as we have used it for more than one year now and want the next one to be more creative and retro/vintage- I have attached a couple of images that display this feeling although these do not have to be used in the flyer- they are just ideas...

I am happy to pay up to $20 for a stock image if this is needed for the final design that we choose...

Target Market(s)

21-40 year old customers who like to have fun

Industry/Entity Type

Apartment

Requirements
Must have
• The flyer needs to have the following information:

$250 voucher to celebrate your next event
Includes:

Priority entry for your crew
A complimentary platter of canapes
A shot cake- yes it is just that- a tower of shots for you and your friends
5 drink cards
No minimum spend

Please book through our website

(In fine print at the bottom of the flyer)
This offer is subject to availability and requires a minimum of 15 guests, voucher not redeemable for cash

Voucher code:

Our business logo needs to be included (please see attached)

(Our address, phone number, email and website)

14 Larchmont Lane St Kilda
(03) 9555 0147
www.17thparlour.com.au
functions@17thparlour.com.au

```html
<!DOCTYPE html>
<html lang="en">
<head>
<meta charset="utf-8">
<title>17th Parlour – $250 Event Voucher</title>
<link rel="stylesheet" href="https://fonts.googleapis.com/css2?family=Lobster&family=Bebas+Neue&family=Oswald:wght@600&display=swap">
<style>
  :root {
    --peach-light: #fbd9c4;
    --peach: #f4b08e;
    --coral: #ee9272;
    --cream: #fde7d2;
    --panel-red: #a3160f;
    --panel-red-dark: #7e0f0a;
    --badge-red: #d8261a;
    --lemon: #f3ef4c;
    --ink: #111111;
    --white: #ffffff;
    --fine-ink: #2b1410;
  }
  * { margin: 0; padding: 0; box-sizing: border-box; }
  html, body { width: 1200px; height: 900px; overflow: hidden; background: var(--cream); }
  .voucher { position: relative; width: 1200px; height: 900px; overflow: hidden; }

  .backdrop {
    position: absolute; inset: 0;
    background:
      radial-gradient(circle at 85% 20%, rgba(255,255,255,0.55), transparent 40%),
      radial-gradient(circle at 20% 85%, rgba(255,255,255,0.5), transparent 45%),
      linear-gradient(120deg, var(--peach-light) 0%, var(--coral) 35%, var(--peach) 60%, var(--cream) 100%);
  }

  .panel { position: absolute; left: 0; top: 0; width: 1200px; height: 900px; }

  .brand {
    position: absolute; left: 42px; top: 48px;
    display: flex; align-items: center; gap: 14px;
    font-family: 'Lobster', cursive;
    font-size: 74px; line-height: 1; color: var(--ink);
  }
  .brand-dot { width: 30px; height: 30px; border-radius: 50%; background: var(--ink); }

  .badge { position: absolute; left: 92px; top: 166px; width: 96px; height: 96px; }
  .badge-value {
    position: absolute; left: 92px; top: 166px; width: 96px; height: 96px;
    display: flex; align-items: center; justify-content: center;
    font-family: 'Bebas Neue', sans-serif; font-size: 34px; color: var(--lemon);
    transform: rotate(-4deg);
  }
  .voucher-title {
    position: absolute; left: 202px; top: 168px;
    font-family: 'Lobster', cursive; font-size: 42px; color: var(--white);
    text-shadow: 2px 2px 0 var(--ink), -1px -1px 0 var(--ink), 1px -1px 0 var(--ink), -1px 1px 0 var(--ink);
    transform: rotate(-3deg);
  }

  .includes-heading {
    position: absolute; left: 56px; top: 278px;
    font-family: 'Bebas Neue', sans-serif; font-size: 38px; color: var(--white);
    text-shadow: 2px 2px 0 var(--ink);
  }
  .perks { position: absolute; left: 52px; top: 324px; list-style: none; }
  .perks li {
    font-family: 'Lobster', cursive; font-size: 30px; line-height: 42.5px;
    color: var(--lemon); font-style: italic;
    text-shadow: 2px 2px 0 var(--ink), -1px -1px 0 var(--ink), 1px -1px 0 var(--ink), -1px 1px 0 var(--ink);
  }

  .booking-note {
    position: absolute; left: 50px; top: 614px;
    font-family: 'Bebas Neue', sans-serif; font-size: 27px; color: var(--white);
  }
  .fine-print {
    position: absolute; left: 0; width: 1120px; top: 819px; text-align: center;
    font-family: 'Oswald', sans-serif; font-weight: 600; font-size: 14px;
    text-transform: uppercase; color: var(--fine-ink); letter-spacing: 0.3px;
  }
</style>
</head>
<body>
<main class="voucher">
  <div class="backdrop" role="img" aria-label="Retro peach and pink striped background scattered with soft white bokeh dots"></div>

  <svg class="panel" viewBox="0 0 1200 900" aria-hidden="true">
    <polygon points="22,150 1192,172 1186,698 18,672" fill="rgba(0,0,0,0.45)"/>
    <polygon points="12,138 1184,162 1176,690 10,664" fill="var(--panel-red)" stroke="var(--panel-red-dark)" stroke-width="2"/>
  </svg>

  <div class="brand"><span class="brand-name">17th parlour</span><span class="brand-dot"></span></div>

  <svg class="badge" viewBox="0 0 96 96" aria-hidden="true">
    <polygon fill="var(--badge-red)" points="48,2 56,12 69,7 72,20 86,22 83,35 94,44 85,54 90,67 77,71 75,85 62,83 54,94 44,85 32,92 26,80 12,79 14,65 3,56 12,46 5,33 18,28 19,15 32,16 38,4"/>
    <circle cx="48" cy="48" r="34" fill="none" stroke="#f7a89b" stroke-width="1.5" stroke-dasharray="4 3"/>
  </svg>
  <div class="badge-value">$ 250</div>
  <h1 class="voucher-title">Voucher</h1>

  <h2 class="includes-heading">Includes:</h2>
  <ul class="perks">
    <li>Priority entry for your crew</li>
    <li>A complimentary platter of canapes</li>
    <li>A shot cake- yes it is just that- a tower of shots for you and your friends</li>
    <li>5 drink cards</li>
    <li>No minimum spend</li>
  </ul>

  <p class="booking-note">Please book through our website</p>

  <p class="fine-print">This offer is subject to availability and requires a minimum of 15 guests, voucher not redeemable for cash</p>
</main>
</body>
</html>
```